One pager fact sheet for healthcare companies

We are looking for a designer to create a theme based off this example. The project will consist of building a layout and theme for a one page, front and back handout. The handout will be used as part of an educational series for medical professionals. The format must be suitable for print production. The theme should be clear, concise, and professional. Cluttered graphics will not be useable.
This project has potential to include additional work over the next 3 months.

Target Market(s)

Healthcare professionals

Industry/Entity Type

Healthcare

Font styles to use
Serif
Sans Serif

Requirements
Must have
• A professional look and feel
Should not have
• Cluttered graphics or busy look

```html
<!DOCTYPE html>
<html lang="en">
<head>
<meta charset="utf-8">
<title>Northlake – Fact Sheet</title>
<link href="https://fonts.googleapis.com/css2?family=Lato:wght@400;700&family=Roboto+Condensed:wght@700&display=swap" rel="stylesheet">
<style>
  :root {
    --green: #8cc03e;
    --blue: #0b55a3;
    --ink: #1d1d1d;
    --panel: #e8e8e9;
    --panel-dark: #bdbdbe;
    --bar: #6a6a6b;
    --paper: #ffffff;
  }
  * { margin: 0; padding: 0; box-sizing: border-box; }
  html, body { width: 1029px; height: 1200px; overflow: hidden; background: #fff; }
  body { font-family: "Lato", sans-serif; color: var(--ink); }
  .canvas { position: relative; width: 1029px; height: 1200px; }
  .sheet { position: absolute; left: 147px; top: 83px; width: 730px; height: 1032px; background: var(--paper); box-shadow: 0 4px 12px rgba(0,0,0,.22); overflow: hidden; }
  .sheet > * { position: absolute; }
  .band-green-top { left: 0; top: 0; width: 100%; height: 17px; background: var(--green); }
  .band-green-bottom { left: 0; bottom: 0; width: 100%; height: 25px; background: var(--green); }
  .cond { font-family: "Roboto Condensed", sans-serif; font-weight: 700; }
  .brand { left: 29px; top: 36px; font-family: "Roboto Condensed", sans-serif; font-weight: 700; font-size: 62px; line-height: 1; color: var(--blue); white-space: nowrap; }
  .contact { left: 397px; top: 31px; font-size: 10.5px; font-weight: 700; }
  .contact div { display: flex; height: 20.5px; align-items: center; }
  .contact span { width: 56px; }
  .contact i { width: 100px; border-bottom: 1px dotted #333; height: 8px; }
  .panel-grey { left: 347px; top: 138px; width: 383px; height: 420px; background: var(--panel); }
  .tab { display: flex; align-items: center; justify-content: center; overflow: hidden; }
  .tab span { writing-mode: vertical-rl; transform: rotate(180deg); white-space: nowrap; color: #fff; font-family: "Roboto Condensed", sans-serif; font-weight: 700; font-size: 26px; line-height: 1; }
  .tab-facts { left: 0; top: 223px; width: 43px; height: 240px; background: var(--green); }
  .tab-structure { left: 356px; top: 228px; width: 40px; height: 240px; background: var(--blue); }
  .heading { font-family: "Roboto Condensed", sans-serif; font-weight: 700; color: var(--blue); font-size: 16.5px; line-height: 1.2; }
  .list { list-style: none; font-size: 10.8px; line-height: 13px; }
  .list li { position: relative; padding-left: 9px; }
  .list li::before { content: ""; position: absolute; left: 0; top: 4px; width: 4px; height: 4px; border-radius: 50%; background: var(--green); }
  .list.blue li::before { background: var(--blue); }
  .org-type { left: 53px; top: 160px; font-size: 13px; font-weight: 700; }
  .org-type span { font-weight: 400; font-size: 10.5px; margin-left: 3px; }
  .lead-head { left: 54px; top: 182px; }
  .lead-a { left: 53px; top: 236px; width: 150px; }
  .lead-b { left: 210px; top: 236px; width: 120px; }
  .phys-head { left: 57px; top: 313px; }
  .phys-table { left: 61px; top: 347px; font-size: 10.8px; border-collapse: collapse; }
  .phys-table th { text-align: left; font-weight: 700; width: 116px; height: 21.5px; }
  .phys-table td { white-space: nowrap; }
  .reach-label { left: 56px; top: 462px; font-size: 21px; }
  .reach-value { left: 62px; top: 495px; font-size: 33px; color: var(--blue); }
  .geo-title { left: 347px; top: 161px; width: 398px; text-align: center; font-size: 23px; font-weight: 700; }
  .geo-sub { left: 347px; top: 190px; width: 398px; text-align: center; font-size: 18px; }
  .hosp-head { left: 415px; top: 255px; }
  .hosp-list { left: 419px; top: 277px; line-height: 17px; }
  .aff-head { left: 416px; top: 334px; }
  .aff-list { left: 419px; top: 364px; width: 300px; }
  .aff-list li { margin-bottom: 4px; }
  .services-band { left: 0; top: 576px; width: 100%; height: 37px; background: var(--blue); color: var(--green); text-align: center; font-size: 29px; line-height: 37px; }
  .share-panel { left: 399px; top: 613px; width: 331px; height: 140px; background: var(--panel-dark); }
  .share-table { left: 421px; top: 647px; font-size: 10.8px; font-weight: 700; border-collapse: collapse; }
  .share-table th { text-align: left; width: 249px; height: 17.5px; }
  .grey-bar { left: 0; top: 742px; width: 399px; height: 11px; background: var(--bar); }
  .svc-head { left: 38px; top: 628px; color: var(--ink); font-size: 16.5px; }
  .svc-a { left: 37px; top: 664px; width: 177px; text-align: justify; }
  .svc-b { left: 236px; top: 664px; width: 150px; text-align: justify; }
  .plans-head { left: 36px; top: 764px; font-size: 19px; }
  .plans-a { left: 37px; top: 798px; line-height: 19.7px; }
  .plans-b { left: 214px; top: 800px; line-height: 19.7px; }
  .risk-head { left: 36px; top: 903px; }
  .risk-list { left: 37px; top: 936px; width: 320px; }
  .risk-list li { margin-bottom: 8px; }
  .divider { left: 376px; top: 770px; width: 2px; height: 232px; background: #e2e2e2; }
  .payer-head { left: 400px; top: 773px; }
  .payer-list { left: 400px; top: 808px; width: 308px; text-align: justify; }
  .payer-list li { margin-bottom: 4px; }
</style>
</head>
<body>
<div class="canvas">
  <article class="sheet">
    <div class="band-green-top"></div>

    <div class="brand">NORTHLAKE</div>
    <div class="contact">
      <div><span>Address</span>:<i></i></div>
      <div><span>Website</span>:<i></i></div>
      <div style="margin-top:3px"><span>Name</span>:<i></i></div>
      <div><span>Address</span>:<i></i></div>
    </div>

    <div class="panel-grey"></div>

    <div class="tab tab-facts"><span>KEY FACTS</span></div>
    <p class="org-type">Organization Type:<span>Not for Profit Health System</span></p>
    <h2 class="heading lead-head">Leadership Team and<br>Contact Information:</h2>
    <ul class="list lead-a">
      <li>Helen R. Marlowe, CEO</li>
      <li>Dorian K. Whitfield, III, President</li>
    </ul>
    <ul class="list lead-b">
      <li>Samuel T. Ardent, EVP and COO</li>
      <li>Peter Kovalenko, Jr. MD, EVP and Chief Medical Officer</li>
    </ul>
    <h2 class="heading phys-head">Physicians in Network:</h2>
    <table class="phys-table">
      <tr><th style="padding-top:8px">Total:</th><td>2,400 Salaried, 3,000 Affiliated</td></tr>
      <tr><th>PCPs:</th><td style="padding-left:1px">1,000 Salaried, 1,500 Affiliated</td></tr>
      <tr><th>Ophthalmologists:</th><td>35 Salaried, 0 Affiliated</td></tr>
      <tr><th>Retina Specialists:</th><td>10 Salaried, 0 Affiliated</td></tr>
    </table>
    <p class="reach-label">10 Salaried, 0 Affiliated:</p>
    <p class="reach-value">800,000</p>

    <div class="tab tab-structure"><span>SYSTEM STRUCTURE</span></div>
    <h2 class="geo-title">Geographic Coverage:</h2>
    <p class="geo-sub">Michigan</p>
    <h2 class="heading hosp-head">Number of Hospitals and Facilities:</h2>
    <ul class="list blue hosp-list">
      <li>7 Hospitals</li>
      <li>Over 35 medical centers and facilities across multiple</li>
      <li>counties in Michigan</li>
    </ul>
    <h2 class="heading aff-head">Key Affiliations:</h2>
    <ul class="list blue aff-list">
      <li>Medical Group has more than 1,100 physicians that staff NL hospital, Cedar Ridge hospital, and 26 medical centers</li>
      <li>Physician Network is a physician-led subsidiary, comprising the Medical Group, hospital-employed and private</li>
      <li>2,000 affiliated private practice physicians</li>
    </ul>

    <h2 class="services-band cond">SERVICES</h2>

    <h2 class="heading svc-head">Key Services and Facilities:</h2>
    <ul class="list svc-a">
      <li>Major service lines: cardiac care, women’s and children’s services, cancer care, orthopedics, transplants, neuroscience, trauma, and urology</li>
    </ul>
    <ul class="list svc-b">
      <li>Key Facilities: ClearView Eye centers include offices for ophthalmologists and retina specialists</li>
    </ul>
    <div class="grey-bar"></div>

    <div class="share-panel"></div>
    <table class="share-table">
      <tr><th>In Facilities</th><td>40%</td></tr>
      <tr><th>In Owned Practices</th><td>30%</td></tr>
      <tr><th>In Affiliated Practices:.</th><td>20%</td></tr>
      <tr><th>Unaffiliated/ Out of Network:.</th><td>10%</td></tr>
    </table>

    <h2 class="heading plans-head">Key Plans:</h2>
    <ul class="list plans-a">
      <li>Averra Health</li>
      <li>Lakeshore Shield</li>
      <li>BlueRiver Care Network</li>
      <li>Harbor Health Plans</li>
      <li>McAllister Health</li>
    </ul>
    <ul class="list plans-b">
      <li>Medicare</li>
      <li>Michigan Medicaid</li>
      <li>Meridale</li>
      <li>Prime Path Health</li>
      <li>Unity Health Plans</li>
    </ul>
    <h2 class="heading risk-head">Level of Risk Taken:</h2>
    <ul class="list risk-list">
      <li>80% of revenue is billed under a risk-based payment scheme</li>
      <li>Half of these lives include the risk for outpatient, physician-administered biologics</li>
    </ul>

    <div class="divider"></div>

    <h2 class="heading payer-head">Key Payer Relationships and Payment Models</h2>
    <ul class="list payer-list">
      <li>COMPANY accepts a variety of risk-based payment models including full and partial risk, bundled payments, and ACO contracts.</li>
      <li>All decisions to join an ACO or participate in a risk-based contract are made at the corporate level</li>
      <li>COMPANY is contracted with CMS as a Next Generation ACO. Through the HMO product, this contract represents 30% of the health system’s revenue and covers over 20,000 Medicare lives</li>
      <li>The remaining share of revenue typically includes a value-based payment model. Contracts with private payers, such as Lakeshore Shield, incorporate contracts based on performance and quality of care which may lead to bonus payments.</li>
    </ul>

    <div class="band-green-bottom"></div>
  </article>
</div>
</body>
</html>
```